Powerpt Design Template for QV7LM

A powerpt design template for QV7lm. A simple layout utilizing my company in the design. www.qv7lm.example . Please use the color pallet from the website and the name, etc. You can use general content from the website but I also need to be able to add slides and utilize the design for multiple purposes.

Target Market(s)

Education

Requirements
Must have
• utlize the design and colors from www.qv7lm.example
Nice to have
• use some general content from the website for "about" qv7lm. More importantly, i need to be able to add slides

```html
<!DOCTYPE html>
<html lang="en">
<head>
<meta charset="utf-8">
<title>QV7lm Presentation Template</title>
<link href="https://fonts.googleapis.com/css2?family=Open+Sans:wght@300;400;600;700&display=swap" rel="stylesheet">
<style>
:root{
  --orange:#f26b3a;--orange-soft:#f79a5c;--peach:#fbd3bd;--yellow:#f5c842;--red:#e8443a;
  --gray:#7a7a7a;--gray-dark:#555;--gray-light:#e9e9e9;--text:#9a9a9a;--white:#fff;
}
*{margin:0;padding:0;box-sizing:border-box}
html,body{width:800px;height:1200px;overflow:hidden;background:#fff;font-family:'Open Sans',sans-serif}
.deck{display:grid;grid-template-columns:repeat(3,262px);grid-auto-rows:148px;column-gap:4px;row-gap:23px;padding:12px 0 0 3px}
.slide{position:relative;overflow:hidden;background:var(--white);box-shadow:0 1px 3px rgba(0,0,0,.28)}
.brand{font:400 9px 'Open Sans',sans-serif;color:var(--gray);display:inline-flex;align-items:center;gap:3px}
.brand::before{content:"";width:6px;height:6px;background:var(--orange)}
.brand.lg{font-size:17px;gap:5px}.brand.lg::before{width:11px;height:11px}
.foot{position:absolute;left:7px;bottom:3px;font-size:7px}
.foot::before{width:5px;height:5px}
.bar{position:absolute;right:0;bottom:2px;width:58%;height:2px;background:var(--yellow)}
.bar::after{content:"";position:absolute;right:12px;bottom:0;width:18px;height:6px;background:linear-gradient(100deg,transparent 30%,var(--orange) 30% 55%,transparent 55% 65%,var(--yellow) 65%)}
.h{position:absolute;left:12px;top:10px;font:400 10.5px 'Open Sans',sans-serif;color:var(--gray-dark)}
.h::after{content:"";display:block;width:24px;height:1px;background:var(--yellow);margin-top:3px}
.lo{font-size:3.5px;line-height:1.45;color:var(--text)}
.hd{font-size:5px;color:var(--orange);font-weight:600}
.img{position:absolute}
.pill{display:inline-block;background:var(--red);color:#fff;font-size:3.5px;padding:1.5px 6px;border-radius:4px}
.ttl{font-weight:400;color:var(--gray-dark)}
.cover{display:flex;flex-direction:column;align-items:center;justify-content:center;text-align:center}
.cover .ttl{font-size:16px}
.cover .sub{font-size:3.5px;color:var(--gray);margin:1px 0 6px}
.cover .rule{width:76px;height:2px;background:linear-gradient(90deg,var(--red) 50%,var(--yellow) 50%);margin-bottom:5px}
.cover .brand{margin-bottom:5px}
.divider .img{inset:0}
.divider .cut{position:absolute;inset:0}
.divider .dt{position:absolute;right:22px;top:66px;text-align:right;color:#fff;font-size:13px;font-weight:400}
.divider .dt small{display:block;font-size:3.5px;margin-top:3px}
.divider .brand{position:absolute;left:7px;bottom:13px}
.card{position:absolute;color:#fff;padding:5px;text-align:center}
.card b{display:block;font-size:4px;margin:3px 0 3px}
.card .lo{color:rgba(255,255,255,.85);font-size:3px}
.ico{width:12px;height:12px;border-radius:50%;background:#fff;margin:2px auto 0}
.grid2{position:absolute;left:12px;top:36px;right:12px;display:grid;grid-template-columns:1fr 1fr;column-gap:14px;row-gap:6px}
.tbl{position:absolute;left:20px;top:44px;width:222px;border-collapse:collapse;font-size:3.5px;color:var(--gray)}
.tbl th{background:var(--orange);color:#fff;font-weight:400;padding:1.6px}
.tbl td{padding:1.6px;text-align:center;border-bottom:0.5px solid #eee}
.tbl td:first-child{color:var(--orange-soft);text-align:left}
.tbl tr:nth-child(even) td{background:#f3f3f3}
.member{position:absolute;top:72px;width:46px;text-align:center}
.member .ph{width:28px;height:28px;border-radius:50%;margin:0 auto 3px;border:1.5px solid #fff;background:linear-gradient(#c9c9c9,#8f8f8f)}
.member b{display:block;font-size:3.5px;color:var(--gray);font-weight:400}
.member i{display:block;font-size:3px;color:var(--orange);font-style:normal;margin-bottom:2px}
.dots{display:flex;gap:2px;justify-content:center;margin-top:3px}
.dots span{width:3px;height:3px;border-radius:50%;background:var(--red)}
.badge{position:absolute;width:28px;height:28px;border-radius:50%;border:1.5px solid #bbb;background:#f2f2f2}
.wm{position:absolute;height:10px;background:#c4c4c4;border-radius:2px}
.kp{position:absolute;top:76px;width:30px;height:30px;border-radius:50%;color:#fff;font-size:3.5px;text-align:center;padding-top:17px}
.kp::before{content:"";position:absolute;left:10px;top:6px;width:10px;height:9px;background:rgba(255,255,255,.85);border-radius:2px}
.legend{display:flex;align-items:flex-start;gap:5px;margin-bottom:7px}
.legend i{flex:none;width:9px;height:9px;border-radius:50%;background:var(--orange)}
.contact{position:absolute;left:142px;top:52px;color:#fff;font-size:4px;line-height:1.3}
.contact p{display:flex;gap:4px;margin-bottom:6px;align-items:flex-start}
.contact p::before{content:"";flex:none;width:4px;height:4px;border-radius:50%;background:#fff;margin-top:.5px}
.icon-sheet{box-shadow:none}
</style>
</head>
<body>
<main class="deck">

  <section class="slide cover">
    <h1 class="ttl">Your Title Goes Here</h1>
    <p class="sub">Your Subtitle Goes Here</p>
    <div class="rule"></div>
    <span class="brand lg">QV7lm</span>
    <span class="pill">Dr. Alan Reyes, Principal</span>
  </section>

  <section class="slide">
    <div class="img" style="inset:0;background:linear-gradient(135deg,#f58a55,#ee6434)" role="img" aria-label="Orange-toned photo of a desk with a clock and glasses"></div>
    <svg class="img" style="inset:0" width="262" height="148"><polygon points="262,42 262,148 140,148" fill="#fff"/></svg>
    <div style="position:absolute;left:34px;top:52px;color:#fff">
      <h1 style="font-size:15px;font-weight:400">Your Title Goes Here</h1>
      <p style="font-size:3.5px;margin:2px 0 5px">Your Subtitle Goes Here</p>
      <span class="pill">Dr. Alan Reyes, Principal</span>
    </div>
    <span class="brand" style="position:absolute;right:7px;bottom:14px;font-size:10px">QV7lm</span>
  </section>

  <section class="slide">
    <div class="img" style="left:12px;top:24px;width:2px;height:1px"></div>
    <div class="img" style="left:12px;top:24px;width:24px;height:1px;background:var(--yellow)"></div>
    <div class="img" style="left:24px;top:34px;width:110px;height:98px;background:linear-gradient(160deg,#f26b3a 0%,#f79a5c 40%,#f5c842 60%,#fbd3bd 100%);opacity:.85" role="img" aria-label="Decorative cluster of orange and yellow triangles"></div>
    <div style="position:absolute;left:134px;top:37px">
      <p style="font-size:10px;color:var(--gray-dark)">Our Agenda</p>
      <ul style="list-style:none;font-size:6px;color:var(--gray);line-height:1.95;margin-top:2px">
        <li>Agenda 1</li><li>Agenda 2</li><li>Agenda 3</li><li>Agenda 4</li><li>Agenda 5</li>
      </ul>
    </div>
    <span class="brand foot">QV7lm</span><div class="bar"></div>
  </section>

  <section class="slide">
    <h2 class="h">Welcome Message</h2>
    <div class="img" style="left:0;top:28px;width:110px;height:120px;background:linear-gradient(#f4f4f4,#d8d8d8)" role="img" aria-label="Portrait photo of the principal"></div>
    <span class="brand lg" style="position:absolute;left:160px;top:36px;font-size:14px">QV7lm</span>
    <div style="position:absolute;left:138px;top:60px;width:108px" class="lo">
      <p style="margin-bottom:4px">Our school team works daily to give every learner a clear path forward, with caring staff, strong programs and steady support for families across the whole district year.</p>
      <p>We welcome you to explore our work, meet our people and join us in building a place where students grow with confidence.</p>
    </div>
    <div class="bar"></div>
  </section>

  <section class="slide">
    <div class="img" style="left:0;top:22px;width:180px;height:112px;background:linear-gradient(135deg,#7d7a74,#3f3d3a 60%,#b9b4aa)" role="img" aria-label="Photo of library shelves with pencils and books"></div>
    <div style="position:absolute;left:131px;top:32px;width:131px;height:82px;background:var(--orange);color:#fff;padding:14px 10px">
      <div style="width:7px;height:7px;border:1px solid #fff;border-radius:1px;margin-bottom:4px"></div>
      <p style="font-size:9px;font-weight:300">PURPOSE/Mission:</p>
      <p class="lo" style="color:#fff;margin-top:3px">Our purpose is to give quality leadership, research and guidance to educators so each classroom improves.</p>
    </div>
    <span class="brand foot">QV7lm</span><div class="bar"></div>
  </section>

  <section class="slide">
    <h2 class="h">How We Do It</h2>
    <div class="img" style="left:12px;top:37px;width:240px;height:50px;background:linear-gradient(90deg,#2f3233,#5a5e60 60%,#f6c348)" role="img" aria-label="Photo of chalk and colored pencils on a slate"></div>
    <div style="position:absolute;left:131px;top:37px;width:121px;height:50px;background:var(--orange);padding:6px 8px;color:#fff">
      <div style="width:6px;height:6px;border:1px solid #fff;margin-bottom:3px"></div>
      <p class="lo" style="color:#fff">We reach this goal by focusing on action based research that leads to practice and benefits policy makers.</p>
    </div>
    <p class="lo" style="position:absolute;left:12px;top:94px;width:240px">From early childhood to college and career readiness, quality instruction and improvement begin with the strengths in teaching and learning. We take the best of current research and align it with practice across the state.</p>
    <span class="brand foot">QV7lm</span><div class="bar"></div>
  </section>

  <section class="slide divider">
    <div class="img" style="background:linear-gradient(135deg,#f7885a,#ef6a3c)" role="img" aria-label="Orange-toned photo of a wooden floor and bookcase"></div>
    <svg class="cut" width="262" height="148"><polygon points="0,90 95,148 0,148" fill="#fff"/></svg>
    <p class="dt">This Is Your Divider Page<small>Your Subtitle Goes Here</small></p>
    <span class="brand" style="font-size:10px;bottom:14px">QV7lm</span>
  </section>

  <section class="slide">
    <h2 class="h">Our Three Column Area</h2>
    <div style="position:absolute;left:14px;right:14px;top:44px;display:grid;grid-template-columns:repeat(3,1fr);gap:14px;text-align:center">
      <div><div style="width:16px;height:12px;border:1px solid var(--orange);margin:0 auto 6px"></div><p class="hd" style="font-size:3.8px">Lorem ipsum dolor</p><p class="lo" style="margin-top:5px">Short sample copy for this column that explains one idea in a few brief lines of text.</p><p class="lo" style="margin-top:4px">More sample copy sits here as a second small paragraph.</p></div>
      <div><div style="width:16px;height:12px;border:1px solid var(--yellow);margin:0 auto 6px"></div><p class="hd" style="font-size:3.8px;color:var(--yellow)">Lorem ipsum dolor</p><p class="lo" style="margin-top:5px">Short sample copy for this column that explains one idea in a few brief lines of text.</p><p class="lo" style="margin-top:4px">More sample copy sits here as a second small paragraph.</p></div>
      <div><div style="width:13px;height:13px;border:1px solid var(--red);border-radius:50%;margin:0 auto 5px"></div><p class="hd" style="font-size:3.8px;color:var(--red)">Lorem ipsum dolor</p><p class="lo" style="margin-top:5px">Short sample copy for this column that explains one idea in a few brief lines of text.</p><p class="lo" style="margin-top:4px">More sample copy sits here as a second small paragraph.</p></div>
    </div>
    <span class="brand foot">QV7lm</span><div class="bar"></div>
  </section>

  <section class="slide">
    <h2 class="h">Our Service</h2>
    <div class="card" style="left:12px;top:33px;width:55px;height:99px;background:var(--orange)"><div class="ico"></div><b>Actionable Research</b><p class="lo">We provide research, both qualitative and quantitative, to support initiatives.</p></div>
    <div class="card" style="left:71px;top:33px;width:55px;height:99px;background:var(--gray)"><div class="ico"></div><b>Ed Policy &amp; Leadership</b><p class="lo">Skilled team works with policy leaders to bring change and guide plans.</p></div>
    <div class="card" style="left:130px;top:33px;width:55px;height:99px;background:var(--orange-soft)"><div class="ico"></div><b>Practice / Implementation</b><p class="lo">We turn findings into daily practice in schools with clear steps.</p></div>
    <div class="card" style="left:189px;top:33px;width:60px;height:99px;background:var(--red)"><div class="ico"></div><b>Negotiation Buying &amp; Review</b><p class="lo">We help districts review options and choose the right tools.</p></div>
    <span class="brand foot">QV7lm</span><div class="bar"></div>
  </section>

  <section class="slide">
    <h2 class="h">Our Bullets Area</h2>
    <div class="grid2">
      <div><p class="hd">● Heading Goes Here</p><p class="lo">Short sample copy for this point in two brief lines of filler text.</p></div>
      <div><p class="hd">● Heading Goes Here</p><p class="lo">Short sample copy for this point in two brief lines of filler text.</p></div>
      <div><p class="hd">● Heading Goes Here</p><p class="lo">Short sample copy for this point in two brief lines of filler text.</p></div>
      <div><p class="hd">● Heading Goes Here</p><p class="lo">Short sample copy for this point in two brief lines of filler text.</p></div>
      <div><p class="hd">● Heading Goes Here</p><p class="lo">Short sample copy for this point in two brief lines of filler text.</p></div>
      <div><p class="hd">● Heading Goes Here</p><p class="lo">Short sample copy for this point in two brief lines of filler text.</p></div>
    </div>
    <span class="brand foot">QV7lm</span><div class="bar"></div>
  </section>

  <section class="slide">
    <div class="img" style="left:0;top:0;width:262px;height:82px;background:linear-gradient(#f48a58,#ef6a3c)" role="img" aria-label="Orange-toned photo of a team in silhouette"></div>
    <h2 class="h" style="color:#fff">Our Team</h2>
    <div class="member" style="left:16px"><div class="ph" role="img" aria-label="Team member photo"></div><b>Ray Dolan</b><i>VP Marketing</i><p class="lo">Short role notes here.</p><div class="dots"><span></span><span></span><span></span></div></div>
    <div class="member" style="left:77px"><div class="ph" role="img" aria-label="Team member photo"></div><b>Ken Alder</b><i>VP Finance</i><p class="lo">Short role notes here.</p><div class="dots"><span></span><span></span><span></span></div></div>
    <div class="member" style="left:138px"><div class="ph" role="img" aria-label="Team member photo"></div><b>Tom Brandt</b><i>VP Development</i><p class="lo">Short role notes here.</p><div class="dots"><span></span><span></span><span></span></div></div>
    <div class="member" style="left:199px"><div class="ph" role="img" aria-label="Team member photo"></div><b>Lia Moreno</b><i>Manager</i><p class="lo">Short role notes here.</p><div class="dots"><span></span><span></span><span></span></div></div>
    <span class="brand foot">QV7lm</span><div class="bar"></div>
  </section>

  <section class="slide">
    <div class="badge" style="left:14px;top:8px"></div>
    <div class="badge" style="left:80px;top:8px"></div>
    <div class="badge" style="left:150px;top:8px"></div>
    <div class="badge" style="left:220px;top:10px;width:32px;height:22px;border-radius:50%"></div>
    <div class="wm" style="left:14px;top:68px;width:28px"></div>
    <div style="position:absolute;left:66px;top:49px;width:196px;height:47px;background:var(--orange);color:#fff;font-size:10px;display:flex;align-items:center;justify-content:center">OUR PREVIOUS WORK</div>
    <div class="wm" style="left:22px;top:113px;width:30px"></div>
    <div class="wm" style="left:102px;top:113px;width:46px"></div>
    <div class="wm" style="left:194px;top:115px;width:42px;height:7px"></div>
  </section>

  <section class="slide">
    <h2 class="h">Your Title Goes Here</h2>
    <p class="lo" style="position:absolute;left:20px;top:34px;width:120px">Description: short sample line for table notes.</p>
    <table class="tbl">
      <tr><th>Lorem ipsum</th><th>Value</th><th>Value</th><th>Value</th><th>Value</th></tr>
      <tr><td>Lorem ipsum</td><td>10</td><td>15</td><td>16</td><td>18</td></tr>
      <tr><td>Lorem ipsum</td><td>12</td><td>11</td><td>15</td><td>15</td></tr>
      <tr><td>Lorem ipsum</td><td>20</td><td>22</td><td>21</td><td>21</td></tr>
      <tr><td>Lorem ipsum</td><td>10</td><td>23</td><td>12</td><td>11</td></tr>
      <tr><td>Lorem ipsum</td><td>25</td><td>25</td><td>25</td><td>25</td></tr>
      <tr><td>Lorem ipsum</td><td>10</td><td>12</td><td>10</td><td>10</td></tr>
      <tr><td>Lorem ipsum</td><td>30</td><td>10</td><td>65</td><td>12</td></tr>
      <tr><td>Lorem ipsum</td><td>26</td><td>33</td><td>35</td><td>32</td></tr>
    </table>
    <span class="brand foot">QV7lm</span><div class="bar"></div>
  </section>

  <section class="slide divider">
    <div class="img" style="background:linear-gradient(135deg,#f7d96a,#f3c63f)" role="img" aria-label="Yellow-toned photo of glasses on an open book"></div>
    <svg class="cut" width="262" height="148"><polygon points="0,40 120,148 0,148" fill="#fff"/></svg>
    <p class="dt" style="top:70px">This Is Your Divider Page<small>Your Subtitle Goes Here</small></p>
    <span class="brand" style="font-size:10px;bottom:14px">QV7lm</span>
  </section>

  <section class="slide">
    <h2 class="h">Bullet &amp; Chart Area</h2>
    <svg class="img" style="left:12px;top:40px" width="130" height="88" font-family="Open Sans, sans-serif" font-size="3" fill="#999">
      <line x1="32" y1="2" x2="32" y2="78" stroke="#ddd" stroke-width=".5"/>
      <g><text x="2" y="14">Category 4</text><rect x="32" y="7" width="70" height="3" fill="#f5c842"/><rect x="32" y="11" width="60" height="3" fill="#f26b3a"/><rect x="32" y="15" width="42" height="3" fill="#f79a5c"/></g>
      <g><text x="2" y="33">Category 3</text><rect x="32" y="26" width="55" height="3" fill="#f5c842"/><rect x="32" y="30" width="68" height="3" fill="#f26b3a"/><rect x="32" y="34" width="22" height="3" fill="#f79a5c"/></g>
      <g><text x="2" y="52">Category 2</text><rect x="32" y="45" width="48" height="3" fill="#f5c842"/><rect x="32" y="49" width="64" height="3" fill="#f26b3a"/><rect x="32" y="53" width="26" height="3" fill="#f79a5c"/></g>
      <g><text x="2" y="71">Category 1</text><rect x="32" y="64" width="36" height="3" fill="#f5c842"/><rect x="32" y="68" width="54" height="3" fill="#f26b3a"/><rect x="32" y="72" width="12" height="3" fill="#f79a5c"/></g>
      <text x="46" y="86">■ Series 1  ■ Series 2  ■ Series 3</text>
    </svg>
    <div style="position:absolute;left:150px;top:45px;width:100px">
      <div class="legend"><i></i><div><p class="hd" style="font-weight:400;font-size:4px">Category One</p><p class="lo">Short sample line of copy here.</p></div></div>
      <div class="legend"><i style="background:var(--orange-soft)"></i><div><p class="hd" style="font-weight:400;font-size:4px">Category Two</p><p class="lo">Short sample line of copy here.</p></div></div>
      <div class="legend"><i style="background:var(--red)"></i><div><p class="hd" style="font-weight:400;font-size:4px">Category Three</p><p class="lo">Short sample line of copy here.</p></div></div>
      <div class="legend"><i style="background:var(--yellow)"></i><div><p class="hd" style="font-weight:400;font-size:4px">Category Four</p><p class="lo">Short sample line of copy here.</p></div></div>
    </div>
    <span class="brand foot">QV7lm</span><div class="bar"></div>
  </section>

  <section class="slide">
    <h2 class="h">Key Points Area</h2>
    <p class="lo" style="position:absolute;left:16px;top:40px;width:230px">Short sample copy that introduces the key points of this slide in one or two brief lines of filler text for layout.</p>
    <div class="kp" style="left:60px;background:var(--orange)">Lorem</div>
    <div class="kp" style="left:90px;background:var(--orange-soft)">Lorem</div>
    <div class="kp" style="left:120px;background:var(--yellow)">Lorem</div>
    <div class="kp" style="left:150px;background:var(--orange-soft)">Lorem</div>
    <div class="kp" style="left:180px;background:var(--orange)">Lorem</div>
    <p class="lo" style="position:absolute;left:50px;top:114px;width:170px;text-align:center">Short closing copy sits under the circles in a few brief centered lines of filler.</p>
    <span class="brand foot">QV7lm</span><div class="bar"></div>
  </section>

  <section class="slide">
    <h2 class="h">Image &amp; Text</h2>
    <div class="img" style="left:12px;top:42px;width:130px;height:72px;background:linear-gradient(90deg,#2f3233,#5a5e60 55%,#f4b83e)" role="img" aria-label="Photo of chalk sticks and pencils on a slate"></div>
    <div style="position:absolute;left:150px;top:38px;width:100px">
      <p class="hd">● Heading Goes Here</p><p class="lo" style="margin-bottom:6px">Short sample copy for this point in three brief lines of filler text here.</p>
      <p class="hd">● Heading Goes Here</p><p class="lo" style="margin-bottom:6px">Short sample copy for this point in three brief lines of filler text here.</p>
      <p class="hd">● Heading Goes Here</p><p class="lo">Short sample copy for this point in three brief lines of filler text here.</p>
    </div>
    <span class="brand foot">QV7lm</span><div class="bar"></div>
  </section>

  <section class="slide">
    <h2 class="h">Workflow Area</h2>
    <p class="lo" style="position:absolute;left:16px;top:34px;width:230px">Short sample copy that introduces the workflow in two brief lines of filler text.</p>
    <svg class="img" style="left:10px;top:50px" width="244" height="86" font-family="Open Sans, sans-serif" font-size="3.5" fill="#f26b3a" text-anchor="middle">
      <path d="M10 64 A22 22 0 0 1 54 64" fill="none" stroke="#f26b3a" stroke-width="6"/>
      <path d="M54 64 A22 22 0 0 0 98 64" fill="none" stroke="#f79a5c" stroke-width="6"/>
      <path d="M98 64 A22 22 0 0 1 142 64" fill="none" stroke="#f26b3a" stroke-width="6"/>
      <path d="M142 64 A22 22 0 0 0 186 64" fill="none" stroke="#f79a5c" stroke-width="6"/>
      <path d="M186 64 A22 22 0 0 1 230 64" fill="none" stroke="#f26b3a" stroke-width="6"/>
      <circle cx="32" cy="42" r="3" fill="#f5c842"/><circle cx="76" cy="86" r="0"/><circle cx="76" cy="82" r="3" fill="#f5c842"/>
      <circle cx="120" cy="42" r="3" fill="#f5c842"/><circle cx="164" cy="82" r="3" fill="#f5c842"/><circle cx="208" cy="42" r="3" fill="#f5c842"/>
      <text x="32" y="66">Data 1</text><text x="76" y="44">Data 2</text><text x="120" y="66">Data 3</text><text x="164" y="44">Data 4</text><text x="208" y="66">Data 5</text>
    </svg>
    <span class="brand foot">QV7lm</span><div class="bar"></div>
  </section>

  <section class="slide divider">
    <div class="img" style="background:linear-gradient(135deg,#9a9a9a,#7d7d7d)" role="img" aria-label="Gray-toned photo of a hand sketching a network of people"></div>
    <svg class="cut" width="262" height="148"><polygon points="0,60 90,148 0,148" fill="#fff"/></svg>
    <p class="dt" style="top:76px">This Is Your Divider Page<small>Your Subtitle Goes Here</small></p>
    <span class="brand" style="font-size:10px;bottom:14px">QV7lm</span>
  </section>

  <section class="slide">
    <div class="img" style="left:0;top:0;width:262px;height:112px;background:linear-gradient(135deg,#f58a55,#ee6434)" role="img" aria-label="Orange-toned photo of pencils in a cup"></div>
    <div style="position:absolute;left:44px;top:48px;color:#fff">
      <p style="font-size:11px;font-weight:600">Thank You</p>
      <p style="font-size:3.5px;margin-top:2px">For Your Precious Time</p>
    </div>
    <div class="contact">
      <p>48 Harbor Lane<br>Fairview 20415</p>
      <p>(555) 014-2273</p>
      <p>hello@qv7lm.example</p>
      <p>www.qv7lm.example</p>
    </div>
    <span class="brand" style="position:absolute;left:104px;bottom:12px;font-size:10px">QV7lm</span>
  </section>

  <section class="slide icon-sheet">
    <svg class="img" style="left:4px;top:2px" width="256" height="68" role="img" aria-label="Sheet of small orange line icons">
      <defs>
        <pattern id="iconTile" width="64" height="22" patternUnits="userSpaceOnUse">
          <g fill="none" stroke="#f26b3a" stroke-width=".8">
            <rect x="1.5" y="1.5" width="7" height="7" rx="1"/>
            <circle cx="16" cy="5" r="3.5"/>
            <path d="M22 5 l2.5 2.5 l4.5 -5"/>
            <path d="M33 5 h7 m-2.5 -2.5 l2.5 2.5 l-2.5 2.5"/>
            <path d="M47 9 c-3 -3 -3 -7 0 -7 c3 0 3 4 0 7z"/>
            <path d="M53 2 h7 v7 h-7z M53 4.5 h7"/>
            <circle cx="5" cy="16" r="3.5"/><path d="M5 14 v2 h2"/>
            <path d="M12.5 19.5 h7 l-3.5 -7z"/>
            <rect x="23" y="12.5" width="8" height="6" rx="1"/><path d="M23 14 l4 2.5 l4 -2.5"/>
            <path d="M35 19 v-3 m3 3 v-5 m3 5 v-7"/>
            <path d="M45 13 l3.5 -1.5 l3.5 1.5 l-3.5 1.5z M46.5 14 v3 h4 v-3"/>
            <path d="M55 19.5 c0 -3 6 -3 6 0 M58 15.5 m-2 0 a2 2 0 1 0 4 0 a2 2 0 1 0 -4 0"/>
          </g>
        </pattern>
      </defs>
      <rect x="0" y="0" width="256" height="66" fill="url(#iconTile)"/>
    </svg>
  </section>

</main>
</body>
</html>
```